11 x 17 Thelanoros Quote

Design the following quote in a poster.

"First say to yourself what you would be; then do what you have to do." - Thelanoros

See here for inspiration - https://prints.quietgrove.com/

Quote

```html
<!DOCTYPE html>
<html lang="en">
<head>
<meta charset="UTF-8">
<title>Thelanoros Quote Poster</title>
<link href="https://fonts.googleapis.com/css2?family=Special+Elite&display=swap" rel="stylesheet">
<style>
  :root {
    --paper: #ffffff;
    --ink: #141414;
    --accent: #a60d07;
    --reverse: #ffffff;
  }
  html, body {
    margin: 0;
    padding: 0;
    width: 776px;
    height: 1200px;
    overflow: hidden;
    background: var(--paper);
  }
  .poster {
    position: relative;
    width: 776px;
    height: 1200px;
    background: var(--paper);
    font-family: "Special Elite", "Courier New", monospace;
    text-transform: uppercase;
    color: var(--ink);
  }
  .quote-line {
    position: absolute;
    left: 0;
    width: 100%;
    margin: 0;
    text-align: center;
    font-size: 64px;
    line-height: 1;
    font-weight: 400;
    letter-spacing: 1px;
  }
  .line-1 { top: 160px; }
  .line-2 { top: 255px; }
  .line-3 { top: 350px; }
  .line-4 { top: 445px; }
  .line-5 { top: 798px; }
  .line-6 { top: 893px; }

  .emphasis {
    position: absolute;
    left: 268px;
    top: 527px;
    width: 240px;
    height: 248px;
  }
  .emphasis-shape {
    position: absolute;
    inset: 0;
    width: 100%;
    height: 100%;
  }
  .emphasis-text {
    position: absolute;
    left: 0;
    width: 100%;
    margin: 0;
    text-align: center;
    color: var(--reverse);
    font-size: 48px;
    line-height: 1;
  }
  .emphasis-then { top: 86px; }
  .emphasis-do { top: 136px; }

  .attribution {
    position: absolute;
    left: 0;
    width: 100%;
    top: 1008px;
    margin: 0;
    text-align: center;
    color: var(--accent);
    font-size: 30px;
    line-height: 1;
    letter-spacing: 1px;
  }
</style>
</head>
<body>
  <main class="poster">
    <blockquote class="quote">
      <p class="quote-line line-1">&ldquo;First say to</p>
      <p class="quote-line line-2">yourself</p>
      <p class="quote-line line-3">what you</p>
      <p class="quote-line line-4">would be;</p>

      <div class="emphasis">
        <svg class="emphasis-shape" viewBox="0 0 240 248" aria-hidden="true">
          <polygon points="120,0 240,122 118,248 0,124" fill="var(--accent)"/>
        </svg>
        <p class="emphasis-text emphasis-then">Then</p>
        <p class="emphasis-text emphasis-do">Do</p>
      </div>

      <p class="quote-line line-5">what you</p>
      <p class="quote-line line-6">have to do.&rdquo;</p>
    </blockquote>
    <p class="attribution">Thelanoros</p>
  </main>
</body>
</html>
```